Stationery for new photography studio
Flyer, Gift Certificate, Business Card, headed paper, CD label and case cover
Please note the change in email address
studio@brightferndesigns.at
Dear sir,
Thanks for your feedback.
#100 is brilliant
I really like #97. I love the colours from the photos. I like the new business cards. Could you combine the concepts in the business cards from #94 #96 #97
temp web address
http://brightferndesigns.snapvault-host.com/
#89 every thing looks great. A few comments:
1) The business cards - I like the logo side however the information side I prefer earlier designs where you used one block colour ie- #87 or #49. I'm still not sure about this side.
2) The dark black logo square on the paper looks too bold.
Great work. Thanks a lot.
Please check the newly uploaded files.
PANTONES:
Blue: 310 C
Brown: 409 C
Pink: 211 C
Gray: 424 C
FONTS:
Petra: Gotham Medium
Valkenor: Gotham Book
Tagline: Gotham Book
Signature: Custom made
I think I prefer the logo in #52 where it is slightly off the page than #70 where it is completely visible.
I like #70, it's sophisticated however the colour scheme is starting depart from the original and from the style of my work, which I think is not so heavy.
If you have any change or better suggestions please let me know.
Thank you.
#61 - #64 I'm not sure if the dots down the sides are necessary.
My website is down. But I'LL let you know when it's back up so you can take a look at some more pictures. I love the use of them in your designs. So excited by what I'm seeing. Thanks for your work so far.
#57. I love it. Everything adds up perfectly. Not sure about the font. It's a bit clumsy. I'd like something sharper and sleeker.
Great direction.
Does this work for A6
A CD disk is 120 mm in diameter (60 mm radius), with a hole 15 mm diameter (7.5 mm radius)
I'm looking on google for CD dimensions. So far I've found the case cover dimensions:
CD Cover Size Specifications for Printing
The finished dimensions for the outside of printed CD covers are 4.724 inches square. Many printed designs include bleed. The "bleed area" is an extra 1/8" of space for design elements or backgrounds to extend beyond the finished size of your piece. A CD cover with bleeds is printed slightly oversized (4.974 inches square) and then cut down to size, giving the appearance that the printing "bleeds" off the edge of the cover rather than having a white border.
Really like the direction of #51 and #52. Re. #55 I prefer the designs where all embellishments or lines are relevant. What I mean by this is that the curve does not tie in anywhere. It's an additional form that is not part of the logo.
#61 and #62 are great. Can you show me some alternative fonts for the 15% and the brightferndesigns.at
This is fun project! What size should be the CD label be? I am not too sure!
#36 with black background?
I'd be interested to see #34 with black replacing the pink.
I have uploaded information to be included in the flyers and gift certificate.
Please look at my photos to understand my style
http://www.facebook.com/BrightFern.Designs?sk=app_274930158846320

```html
<!DOCTYPE html>
<html lang="de">
<head>
<meta charset="utf-8">
<title>Petra Valkenor – Business Cards</title>
<link href="https://fonts.googleapis.com/css2?family=Montserrat:wght@400;500;600&display=swap" rel="stylesheet">
<style>
  :root{
    --bg:#e6e3df;
    --card-white:#ffffff;
    --card-black:#111111;
    --pink:#e58fb0;
    --pink-deep:#e0558e;
    --gray:#7d7b78;
    --gray-dark:#3a3836;
    --gray-light:#b9b6b2;
  }
  *{margin:0;padding:0;box-sizing:border-box}
  html,body{width:1200px;height:850px;overflow:hidden}
  body{background:var(--bg);font-family:"Montserrat",sans-serif;position:relative}

  .card{position:absolute;width:520px;height:300px;border-radius:26px;overflow:hidden;box-shadow:0 4px 14px rgba(0,0,0,.12)}
  .card--info{left:340px;top:60px;background:var(--card-white)}
  .card--dark{left:60px;top:490px;background:var(--card-black)}
  .card--light{left:620px;top:490px;background:var(--card-white)}

  .edge-strip{position:absolute;width:8px;height:42%;background:var(--pink)}
  .edge-strip--left-low{left:0;bottom:12%}
  .edge-strip--left-high{left:0;top:12%}
  .edge-strip--right-low{right:0;bottom:12%}
  .edge-strip--right-high{right:0;top:12%}

  .brand{position:absolute;left:0;right:0;text-align:center}
  .brand__mark{display:block;margin:0 auto 10px;width:28px;height:28px;border:3px solid var(--pink);border-radius:6px}
  .brand__name{font-weight:400;color:var(--gray);letter-spacing:.18em;white-space:nowrap}
  .brand__tagline{color:var(--pink);font-weight:500;letter-spacing:.42em;margin-top:6px}

  .card--info .brand{top:18px}
  .card--info .brand__mark{width:22px;height:22px;margin-bottom:8px}
  .card--info .brand__name{font-size:22px}
  .card--info .brand__tagline{font-size:7px}

  .card--dark .brand,.card--light .brand{top:84px}
  .card--dark .brand__name,.card--light .brand__name{font-size:34px}
  .card--dark .brand__tagline,.card--light .brand__tagline{font-size:10px}
  .card--dark .brand__name{color:var(--gray-light)}

  .contact-list{position:absolute;left:26px;top:176px;list-style:none}
  .contact-list li{display:flex;align-items:center;gap:9px;font-size:10px;color:var(--gray-dark);margin-bottom:10px}
  .contact-list svg{width:11px;height:11px;fill:var(--gray-dark)}

  .address{position:absolute;right:34px;top:176px;text-align:left}
  .address__name{font-size:15px;font-weight:500;color:var(--pink-deep);margin-bottom:8px}
  .address__line{font-size:10px;color:var(--gray-dark);line-height:1.55}
</style>
</head>
<body>

  <section class="card card--info" aria-label="Business card, contact side">
    <div class="brand">
      <span class="brand__mark"></span>
      <p class="brand__name">Petra Valkenor</p>
      <p class="brand__tagline">BRIGHT FERN DESIGNS</p>
    </div>
    <ul class="contact-list">
      <li><svg viewBox="0 0 12 12" aria-hidden="true"><rect x="3" y="0" width="6" height="12" rx="1.2"/></svg>06641287354</li>
      <li><svg viewBox="0 0 12 12" aria-hidden="true"><rect x="0" y="2" width="12" height="8" rx="1"/></svg>Petra@Valkenor.at</li>
      <li><svg viewBox="0 0 12 12" aria-hidden="true"><circle cx="6" cy="6" r="6"/></svg>www.BrightFernDesigns.at</li>
    </ul>
    <div class="address">
      <p class="address__name">Petra Valkenor</p>
      <p class="address__line">Lindengasse 7/4</p>
      <p class="address__line">1070 Wien</p>
    </div>
  </section>

  <section class="card card--dark" aria-label="Business card, logo side on black">
    <span class="edge-strip edge-strip--left-low"></span>
    <span class="edge-strip edge-strip--right-high"></span>
    <div class="brand">
      <span class="brand__mark"></span>
      <p class="brand__name">Petra Valkenor</p>
      <p class="brand__tagline">BRIGHT FERN DESIGNS</p>
    </div>
  </section>

  <section class="card card--light" aria-label="Business card, logo side on white">
    <span class="edge-strip edge-strip--left-high"></span>
    <span class="edge-strip edge-strip--right-low"></span>
    <div class="brand">
      <span class="brand__mark"></span>
      <p class="brand__name">Petra Valkenor</p>
      <p class="brand__tagline">BRIGHT FERN DESIGNS</p>
    </div>
  </section>

</body>
</html>
```